TLB Feedback sticker

We need a sticker design for our secondary school (aged 11 - 18). This is to allow teachers to provide feedback to students and vice-versa, having a conversation with the learner. I would love to have at least two different designs and it to be attractive, so that all can be included. I've attached the basic outline with the information to be presented. It should be A5 size, so that 2 of these can be fitted in.

Target Market(s)

Secondary school students

Industry/Entity Type

School

Font styles to use
Sans Serif

Requirements
Must have
• Attached details of the headings and enough space for all parties to respond.
Should not have
• Anything deemed inappropriate for secondary students

```html
<!DOCTYPE html>
<html lang="en">
<head>
<meta charset="utf-8">
<title>Formative Feedback Sticker</title>
<link rel="stylesheet" href="https://fonts.googleapis.com/css2?family=PT+Sans:wght@400;700&display=swap">
<style>
  :root {
    --sticker-bg: #e6ee96;
    --panel-bg: #ffffff;
    --panel-border: #9b9b9b;
    --rule: #cdcdcd;
    --ink: #1a1a1a;
  }
  * { box-sizing: border-box; margin: 0; padding: 0; }
  html, body { width: 1200px; height: 839px; overflow: hidden; }
  body {
    background: var(--sticker-bg);
    font-family: "PT Sans", Arial, sans-serif;
    color: var(--ink);
    position: relative;
  }
  .panel {
    position: absolute;
    background: var(--panel-bg);
    border: 2px solid var(--panel-border);
    border-radius: 18px;
  }
  .title-bar {
    left: 16px; top: 14px; width: 1160px; height: 54px;
    display: flex; align-items: center;
    padding-left: 104px;
    font-size: 30px;
    border-radius: 14px;
  }
  .title-bar strong { font-weight: 700; letter-spacing: 0.2px; margin-right: 8px; }
  .title-bar .role { font-weight: 400; }
  .title-bar .date { margin-left: 64px; font-weight: 400; display: flex; align-items: baseline; }
  .date .blank {
    display: inline-block; width: 58px; border-bottom: 1.5px solid var(--ink);
    height: 24px; margin-left: 6px;
  }
  .date .sep { margin-left: 4px; font-size: 26px; }

  .teacher-panel { left: 18px; top: 80px; width: 1160px; height: 388px; }
  .student-panel { left: 18px; top: 480px; width: 572px; height: 342px; }
  .reflection-panel { left: 606px; top: 480px; width: 572px; height: 342px; }

  .label-row {
    position: absolute; left: 14px; right: 18px;
    display: flex; align-items: flex-end;
    font-size: 15px; font-weight: 700;
  }
  .label-row .fill { flex: 1; border-bottom: 1.5px solid var(--rule); margin-left: 6px; margin-bottom: 3px; }
  .rule {
    position: absolute; left: 14px; right: 18px;
    border-bottom: 1.5px solid var(--rule);
  }
  .heading {
    position: absolute; left: 14px; top: 14px;
    font-size: 15px; font-weight: 700;
  }
</style>
</head>
<body>
  <header class="panel title-bar">
    <strong>FORMATIVE FEEDBACK</strong><span class="role">Teacher C/L or H/L</span>
    <span class="date">Date:<span class="blank"></span><span class="sep">/</span><span class="blank"></span><span class="sep">/</span><span class="blank"></span></span>
  </header>

  <section class="panel teacher-panel">
    <div class="label-row" style="top:18px">Strengths (What went well…)<span class="fill"></span></div>
    <div class="rule" style="top:62px"></div>
    <div class="rule" style="top:92px"></div>
    <div class="rule" style="top:122px"></div>

    <div class="label-row" style="top:156px">Target (Even better if…)<span class="fill"></span></div>
    <div class="rule" style="top:200px"></div>
    <div class="rule" style="top:230px"></div>
    <div class="rule" style="top:260px"></div>

    <div class="label-row" style="top:290px">Action<span class="fill"></span></div>
    <div class="rule" style="top:334px"></div>
    <div class="rule" style="top:362px"></div>
  </section>

  <section class="panel student-panel">
    <h2 class="heading">Response (Student)</h2>
    <div class="rule" style="top:58px"></div>
    <div class="rule" style="top:88px"></div>
    <div class="rule" style="top:118px"></div>
    <div class="rule" style="top:148px"></div>
    <div class="rule" style="top:178px"></div>
    <div class="rule" style="top:208px"></div>
    <div class="rule" style="top:238px"></div>
    <div class="rule" style="top:268px"></div>
    <div class="rule" style="top:298px"></div>
  </section>

  <section class="panel reflection-panel">
    <h2 class="heading">Response and Reflection (Teacher)</h2>
    <div class="rule" style="top:58px"></div>
    <div class="rule" style="top:88px"></div>
    <div class="rule" style="top:118px"></div>
    <div class="rule" style="top:148px"></div>
    <div class="rule" style="top:178px"></div>
    <div class="rule" style="top:208px"></div>
    <div class="rule" style="top:238px"></div>
    <div class="rule" style="top:268px"></div>
    <div class="rule" style="top:298px"></div>
  </section>
</body>
</html>
```